Marmot Harbor concert poster 0918

Marmot Harbor is a 1990's alternative rock cover band in the Philadelphia area. We need a poster design for an upcoming gig. See 'Must Haves' for key elements.
Our set includes songs by Quillen, RDV, Lark Drivers, Valdosa, Kinder than Marlo, Pendulo, Brass Hour, Vox, Paper Kite Alley, Tin Sparrows, etc. If you know this music, you'll get it. Our set is high energy and upbeat, and we don't take ourselves too seriously.
Style: I leave that to you, but I like many of the recent concert posters done for Korvel, if that's any indication of what I'm looking for. Maybe a subtle 1990s reference, or something to convey the 1990s style or music.
You can find our current logo on www.fanpagehub.example/brindle90s - you may choose to work with this, or not, your option. The award will be based on my subjective overall impression. If you choose to include a new logo design on the poster, we may use it for ongoing projects (T-shirts, etc).

Target Market(s)

Music-minded people from ages 21-55, with sweet spot around the age 40s. The poster will hang in restaurants and shops in suburbia, so images should be chosen accordingly.

Font styles to use
Sans Serif

Colors

Designer to choose colors to be used in the design.

Requirements
Must have
• Highly legible (from 5 meters or so away) - will hang in suburban restaurants and store windows.
• Sized to print 11"x17" poster format
• Date and time of event (Sept 29, 9pm), and venue (Holloway Lounge, Jenkintown).
• A reference to "'90s alt rock" or "'90s alternative rock" is also important.
• Visual interest, and ability for this to serve as a template for future events (by changing the date and venue name)
Nice to have
• Bold color
• A '90's rock feel
• Ok to use our logo art attached, not required
Should not have
• Images that don't fit a restaurant setting (like a live or dead opossum, which looks like a rat)
• Too busy / tough to read
• Monochrome / greyscale

```html
<!DOCTYPE html>
<html lang="en">
<head>
<meta charset="utf-8">
<title>Marmot Harbor – Live at Holloway Lounge</title>
<link href="https://fonts.googleapis.com/css2?family=Oswald:wght@500;600;700&family=Open+Sans:wght@800&display=swap" rel="stylesheet">
<style>
  :root {
    --paper: #d9cba0;
    --ink: #1d2624;
    --teal: #3e8c86;
    --teal-deep: #1f4e4c;
    --teal-light: #9fcfc4;
    --plum: #4a2236;
    --orange: #d46f1c;
    --mustard: #c9901f;
    --cream: #ece7d8;
  }
  * { margin: 0; padding: 0; box-sizing: border-box; }
  html, body { width: 900px; height: 1200px; overflow: hidden; }
  body { background: var(--ink); }

  .poster {
    position: relative;
    width: 900px;
    height: 1200px;
    overflow: hidden;
    background: linear-gradient(180deg, var(--paper) 0%, var(--paper) 24%, #7c8772 33%, var(--teal-deep) 45%, #233432 70%, var(--ink) 100%);
  }

  .art-headdress {
    position: absolute;
    left: 400px; top: 20px;
    width: 500px; height: 1070px;
    border-radius: 50% 0 0 42% / 30% 0 0 20%;
    background: linear-gradient(160deg, var(--teal-deep) 0%, var(--teal) 28%, var(--mustard) 36%, var(--teal) 44%, var(--teal-light) 66%, var(--cream) 80%, var(--teal) 100%);
  }
  .art-eye {
    position: absolute;
    left: 0; top: 440px;
    width: 410px; height: 400px;
    border-radius: 0 50% 50% 0;
    background: linear-gradient(180deg, var(--teal) 0%, var(--teal-deep) 30%, var(--plum) 55%, var(--teal) 80%, var(--teal-deep) 100%);
  }

  .band-title {
    position: absolute;
    left: 40px; top: 34px;
    font-family: "Oswald", sans-serif;
    font-weight: 700;
    font-size: 124px;
    line-height: .8;
    letter-spacing: 14px;
    color: var(--ink);
    text-transform: uppercase;
  }
  .band-title span { display: block; }
  .band-title .line-two { color: var(--teal-deep); }

  .band-mark {
    position: absolute;
    left: 82px; top: 868px;
    font-family: "Oswald", sans-serif;
    text-transform: uppercase;
  }
  .band-mark .name {
    display: flex; align-items: center; gap: 14px;
    font-weight: 600;
    font-size: 44px;
    line-height: 1.1;
    color: var(--cream);
  }
  .band-mark .dot {
    width: 30px; height: 30px; border-radius: 50%;
    background: var(--cream);
  }
  .band-mark .genre {
    margin-left: 44px;
    font-weight: 500;
    font-size: 28px;
    letter-spacing: 3px;
    color: var(--orange);
  }

  .rule {
    position: absolute;
    left: 54px; top: 1004px;
    width: 420px; height: 5px;
    background: var(--cream);
  }

  .event-when {
    position: absolute;
    left: 54px; top: 1012px;
  }
  .event-time {
    font-family: "Oswald", sans-serif;
    font-weight: 500;
    font-size: 56px;
    line-height: 1.05;
    color: var(--orange);
    letter-spacing: -1px;
    text-transform: uppercase;
    white-space: nowrap;
  }
  .event-date {
    font-family: "Open Sans", sans-serif;
    font-weight: 800;
    font-size: 48px;
    line-height: 1.1;
    color: var(--cream);
    text-transform: uppercase;
  }
  .event-date .day { color: var(--orange); }

  .brace {
    position: absolute;
    left: 506px; top: 1010px;
  }

  .event-where {
    position: absolute;
    left: 552px; top: 1016px;
    font-family: "Oswald", sans-serif;
    font-weight: 500;
    font-size: 46px;
    line-height: 1.2;
    color: var(--cream);
    letter-spacing: -1px;
    text-transform: uppercase;
    white-space: nowrap;
  }
</style>
</head>
<body>
  <main class="poster">
    <div class="art-headdress" role="img" aria-label="Illustrated skull wearing a feathered headdress in teal, cream and mustard"></div>
    <div class="art-eye" role="img" aria-label="Stylised illustrated eye with teal and plum grunge splatter and floral flourishes"></div>

    <h1 class="band-title">
      <span class="line-one">Marmot</span>
      <span class="line-two">Harbor</span>
    </h1>

    <div class="band-mark">
      <p class="name"><span class="dot"></span>Marmot Harbor</p>
      <p class="genre">'90s Alt Rock</p>
    </div>

    <div class="rule"></div>

    <div class="event-when">
      <p class="event-time">Starting at 9:00 PM</p>
      <p class="event-date">September <span class="day">29</span></p>
    </div>

    <svg class="brace" width="36" height="120" viewBox="0 0 36 120" aria-hidden="true">
      <path d="M6 4 C22 4 18 28 18 46 C18 55 22 59 30 60 C22 61 18 65 18 74 C18 92 22 116 6 116"
            fill="none" stroke="var(--cream)" stroke-width="4" stroke-linecap="round"/>
    </svg>

    <div class="event-where">
      <p class="venue-name">Holloway Lounge</p>
      <p class="venue-town">Jenkintown</p>
    </div>
  </main>
</body>
</html>
```